Vorelux - A range of environmental public toilet products

We need a design for an existing company with a new direction. We supply toilet cleaning products, matts etc that not only keep your public toilet clean and smelling good but also clean pipes and toilet bowls at the same time.
Many of the products contain a unique enzyme deodorant formulation, which can effectively kill bacterial, deodorize, eliminating smells and clean the Urinal and pipes with every flush.

The web page needs to say we are clean and sparkeling but please note "THIS IS NOT A HOME PRODUCT but for public urinals and bathrooms.
Our product is not expensive but is helping the environment and
completely safe
Updates

Reason: Unfortunately all members of the comapny are still on holiday and I have not been able to contact 2 of them regarding the site and I would like their input. I think they are all back shortly but not sure.

Target Market(s)

Industrial Cleaners and suppliers to hotels, clubs etc

Industry/Entity Type

Environment

Requirements
Must have
• The front page will have:
Point of Difference
Products
Ordering
Testominials
FAQ
Our Policies
Contact Us
Nice to have
• Make it look like you would want to use the piublic toilets.
As you know public toilets can be ugly places/

```html
<!DOCTYPE html>
<html lang="en">
<head>
<meta charset="utf-8">
<title>Vorelux – Toilet deodorant blocks manufacturers</title>
<link href="https://fonts.googleapis.com/css2?family=Arimo:wght@400;700&family=Gelasio:wght@400;700&display=swap" rel="stylesheet">
<style>
  :root {
    --brand-blue: #1f4596;
    --nav-blue: #0a3a93;
    --band-blue: #20479a;
    --band-blue-dark: #1a3e8c;
    --accent-yellow: #f5c400;
    --accent-orange: #f39a1c;
    --white: #ffffff;
    --footer-grey: #e3e3e3;
    --footer-text: #6d6d6d;
    --line-grey: #d6d6d6;
    --leaf-green: #5f8a4a;
    --tablet-pink: #ee6f88;
  }
  * { box-sizing: border-box; margin: 0; padding: 0; }
  html, body { width: 1200px; height: 900px; overflow: hidden; }
  body {
    position: relative;
    background: var(--white);
    font-family: "Arimo", Arial, sans-serif;
    color: var(--footer-text);
  }
  h2, h3 { font-weight: 400; }
  .abs { position: absolute; }

  .top-shade { left: 0; top: 0; width: 1200px; height: 10px; background: linear-gradient(#cfcfcf, #fff); }

  /* header */
  .brand { left: 341px; top: 31px; display: flex; align-items: center; gap: 6px; }
  .brand-name { font-weight: 700; font-size: 30px; color: var(--brand-blue); letter-spacing: 0.5px; }
  .brand-dot { width: 9px; height: 9px; border-radius: 50%; background: var(--accent-orange); margin-top: 14px; }
  .tagline { right: 313px; top: 45px; font-family: "Gelasio", Georgia, serif; font-size: 14px; color: var(--brand-blue); }

  /* blue band */
  .about-band {
    left: 0; top: 255px; width: 1200px; height: 261px;
    background:
      repeating-linear-gradient(45deg, rgba(255,255,255,0.025) 0 2px, transparent 2px 6px),
      linear-gradient(var(--band-blue), var(--band-blue-dark));
    border-bottom: 3px solid #e8e8e8;
  }

  /* decoration placeholders (sit behind the hero frame) */
  .flowers-left {
    left: 278px; top: 122px; width: 70px; height: 160px;
    border-radius: 30px 10px 10px 30px;
    background: linear-gradient(180deg, #6f9a55, var(--leaf-green));
  }
  .tablets {
    left: 290px; top: 262px; width: 165px; height: 62px;
    border-radius: 31px;
    background: linear-gradient(180deg, #f58ba0, var(--tablet-pink));
  }
  .flowers-right {
    left: 818px; top: 262px; width: 116px; height: 42px;
    border-radius: 10px 20px 20px 10px;
    background: linear-gradient(180deg, #6f9a55, var(--leaf-green));
  }

  /* hero panel */
  .hero-frame {
    left: 338px; top: 73px; width: 566px; height: 220px;
    background: var(--white); border-radius: 8px;
    box-shadow: 0 3px 8px rgba(0,0,0,0.25);
  }
  .main-nav { left: 345px; top: 80px; width: 160px; height: 207px; background: var(--nav-blue); }
  .main-nav ul { list-style: none; padding: 9px 0 0 12px; }
  .main-nav li {
    display: flex; align-items: center; gap: 11px;
    height: 22.3px; font-size: 9px; color: var(--white); letter-spacing: 0.2px;
  }
  .main-nav li::before {
    content: ""; width: 7px; height: 7px; border-radius: 50%;
    background: radial-gradient(circle at 40% 40%, #ffe680, var(--accent-yellow));
  }
  .hero-photo {
    left: 511px; top: 80px; width: 384px; height: 207px;
    background: linear-gradient(170deg, #8ab3c4 0%, #5f8fa3 55%, #3c4a4c 100%);
  }
  .hero-caption {
    left: 744px; top: 209px; width: 143px; height: 69px;
    background: rgba(55,60,62,0.82);
    padding: 17px 0 0 20px;
    font-family: "Gelasio", Georgia, serif; font-size: 11px; line-height: 13.5px;
    color: var(--white); letter-spacing: 0.3px;
  }

  /* about */
  .section-marker-hollow { left: 344px; top: 327px; width: 16px; height: 16px; border-radius: 50%; border: 2px solid var(--white); background: rgba(255,255,255,0.15); }
  .about-title { left: 367px; top: 326px; font-family: "Gelasio", Georgia, serif; font-size: 16px; color: var(--white); }
  .about-text { font-size: 8.7px; line-height: 12.1px; color: #e6ecf7; }
  .about-col-1 { left: 346px; top: 360px; width: 160px; }
  .about-col-2 { left: 540px; top: 360px; width: 156px; }
  .about-col-2 p + p { margin-top: 12px; }
  .more-button {
    left: 344px; top: 472px; width: 74px; height: 20px;
    border: 1px solid #c9d6ef; border-radius: 6px;
    background: linear-gradient(#3a63b4, #2a519f);
    font-size: 8px; color: var(--white); text-align: center; line-height: 18px;
  }
  .about-photo {
    left: 729px; top: 362px; width: 162px; height: 102px;
    border: 3px solid #f2f2f2;
    background: linear-gradient(135deg, #d8d8d8, #9c9c9c 60%, #bdbdbd);
  }

  /* products */
  .section-marker-solid { left: 352px; top: 547px; width: 14px; height: 14px; border-radius: 50%; background: var(--brand-blue); }
  .products-title { left: 379px; top: 546px; font-family: "Gelasio", Georgia, serif; font-size: 12px; color: var(--brand-blue); letter-spacing: 0.3px; }
  .products-sub { left: 380px; top: 563px; font-size: 8px; color: #a8a8a8; letter-spacing: 0.2px; }
  .product { top: 590px; height: 120px; }
  .product-image { position: absolute; top: 6px; }
  .product-name { position: absolute; top: 107px; width: 100%; text-align: center; font-size: 8px; color: #a5a5a5; letter-spacing: 0.3px; }
  .product-divider { top: 588px; width: 1px; height: 112px; background: linear-gradient(transparent, var(--line-grey) 20%, var(--line-grey) 80%, transparent); }
  .bucket-white { background: linear-gradient(90deg, #dcdcdc, #fafafa 50%, #d2d2d2); border-top: 8px solid var(--accent-yellow); }
  .bucket-blue { background: linear-gradient(90deg, #d8d8d8, #fafafa 50%, #d0d0d0); border-top: 8px solid #2f63a8; }
  .bucket-yellow { background: linear-gradient(90deg, #d6d2b4, #f8f3d2 50%, #d6cfa4); border-top: 8px solid #e8c317; }
  .crystals { border-radius: 12px; background: linear-gradient(120deg, #a9c6f5 0%, #a9c6f5 40%, #f1e34a 60%, #f1e34a 100%); }
  .next-arrow { left: 818px; top: 626px; }

  /* footer */
  .footer { left: 0; top: 745px; width: 1200px; height: 130px; background: var(--footer-grey); border-top: 3px solid #d0d0d0; }
  .footer-divider { top: 745px; width: 2px; height: 130px; background: var(--white); }
  .footer-heading { font-family: "Gelasio", Georgia, serif; font-size: 10px; color: #777; letter-spacing: 0.3px; }
  .contact-list { left: 355px; top: 791px; font-size: 7.5px; line-height: 12.7px; color: var(--footer-text); }
  .contact-list dt { float: left; width: 37px; clear: left; }
  .contact-list dd { margin-left: 39px; }
  .contact-list .address { margin-top: 4px; line-height: 10px; }
  .footer-links { list-style: none; font-size: 7px; line-height: 12.8px; color: var(--footer-text); letter-spacing: 0.2px; }
  .bottom-bar { left: 0; top: 875px; width: 1200px; height: 25px; background: var(--brand-blue); }
</style>
</head>
<body>
  <div class="abs top-shade"></div>

  <header>
    <div class="abs brand"><span class="brand-name">VORELUX</span><span class="brand-dot"></span></div>
    <div class="abs tagline">Toilet deodorant blocks manufacturers</div>
  </header>

  <div class="abs about-band"></div>

  <div class="abs flowers-left" role="img" aria-label="Red flowering plant decoration"></div>
  <div class="abs flowers-right" role="img" aria-label="Red flowering plant decoration"></div>
  <div class="abs tablets" role="img" aria-label="Pink toilet deodorant tablets"></div>

  <div class="abs hero-frame"></div>
  <nav class="abs main-nav">
    <ul>
      <li>HOME</li>
      <li>PRODUCTS</li>
      <li>ORDERING</li>
      <li>TESTOMINIALS</li>
      <li>FAQ</li>
      <li>OUR POLICIES</li>
      <li>CONTACT US</li>
    </ul>
  </nav>
  <div class="abs hero-photo" role="img" aria-label="Row of clean white urinals against a blue tiled wall"></div>
  <div class="abs hero-caption">DEODORIZES<br>YOUR TOILET AND<br>KILLS &nbsp;BACTERIA</div>

  <section>
    <div class="abs section-marker-hollow"></div>
    <h2 class="abs about-title">ABOUT US</h2>
    <div class="abs about-text about-col-1">
      <p>Are you looking for toilet deodorant blocks? Look no further! Vorelux is an Australian owner operator manufacturer of &nbsp;toilet deodorant blocks that have been supplying Australians &amp; international customers for over 10 years. &nbsp;No matter what size your order is, Vorelux can handle it!</p>
    </div>
    <div class="abs about-text about-col-2">
      <p>We only manufacture high quality toilet deodorant blocks, our blocks are rich in perfume and well known for their low maintenance.</p>
      <p>Vorelux toilet crystals are a dependable, safe and economical long-term odour control for toilets. They</p>
    </div>
    <div class="abs more-button">MORE</div>
    <div class="abs about-photo" role="img" aria-label="Close-up of a white urinal"></div>
  </section>

  <section>
    <div class="abs section-marker-solid"></div>
    <h2 class="abs products-title">OUR PRODUCTS</h2>
    <div class="abs products-sub">FOR MORE DETAILS CLICK HERE</div>

    <div class="abs product" style="left:330px;width:102px;">
      <div class="product-image bucket-white" role="img" aria-label="White tub with yellow lid" style="left:16px;width:68px;height:88px;border-radius:3px 3px 8px 8px;"></div>
      <div class="product-name">PRODUCT NAME</div>
    </div>
    <div class="abs product-divider" style="left:442px;"></div>
    <div class="abs product" style="left:445px;width:102px;">
      <div class="product-image bucket-blue" role="img" aria-label="White tub with blue lid" style="left:18px;top:22px;width:62px;height:74px;border-radius:3px 3px 8px 8px;"></div>
      <div class="product-name">PRODUCT NAME</div>
    </div>
    <div class="abs product-divider" style="left:549px;"></div>
    <div class="abs product" style="left:560px;width:102px;">
      <div class="product-image bucket-yellow" role="img" aria-label="Yellow tub of toilet blocks" style="left:14px;top:30px;width:64px;height:68px;border-radius:3px 3px 8px 8px;"></div>
      <div class="product-name">PRODUCT NAME</div>
    </div>
    <div class="abs product-divider" style="left:662px;"></div>
    <div class="abs product" style="left:670px;width:153px;">
      <div class="product-image crystals" role="img" aria-label="Blue and yellow toilet deodorant crystals" style="left:8px;top:20px;width:128px;height:64px;"></div>
      <div class="product-name">PRODUCT NAME</div>
    </div>
    <div class="abs product-divider" style="left:820px;"></div>
    <svg class="abs next-arrow" width="62" height="42" viewBox="0 0 62 42" aria-hidden="true">
      <path d="M2 3 A18 18 0 0 1 2 39" fill="none" stroke="#1f4596" stroke-width="6"/>
      <rect x="14" y="12" width="46" height="18" rx="4" fill="#1f4596"/>
    </svg>
  </section>

  <footer>
    <div class="abs footer"></div>
    <div class="abs footer-divider" style="left:513px;"></div>
    <div class="abs footer-divider" style="left:680px;"></div>

    <h3 class="abs footer-heading" style="left:352px;top:768px;">CONTACT US</h3>
    <dl class="abs contact-list">
      <dt>Fax:</dt><dd>02 5550 1837</dd>
      <dt>Mobile:</dt><dd>0400 555 219 &nbsp;( Martin )</dd>
      <dt>Email:</dt><dd>martin@vorelux.example</dd>
      <dt class="address">Address:</dt><dd class="address">12/3 Harbour Ln<br>Lakeview, NSW, 2199</dd>
    </dl>

    <h3 class="abs footer-heading" style="left:549px;top:768px;">NAVIGATION</h3>
    <ul class="abs footer-links" style="left:550px;top:790px;">
      <li>HOME</li><li>PRODUCTS</li><li>ORDERING</li><li>TESTOMINIALS</li>
    </ul>
    <ul class="abs footer-links" style="left:723px;top:796px;">
      <li>FAQ</li><li>OUR POLICIES</li><li>CONTACT US</li>
    </ul>

    <div class="abs bottom-bar"></div>
  </footer>
</body>
</html>
```